Web and Mobile banner ad designs for vokra

I need both web and mobile ad designs for the launch of a new app called vokra.

These are the sizes that I am looking at for both the web and mobile banners:

1) WEB banner - static
728 x 90
300 x 250

2) MOBILE banner - static
320 x 50 Pixels XX-Large Image Banner
300 x 50 Pixels X-Large Image Banner
216 x 36 Pixels Large Image Banner
168 x 28 Pixels Medium Image Banner
120 x 20 Pixels Small Image Banner

Format: jpeg, png, gif

Copy: I have 2 versions of copy that I need for each of the banner sizes as listed above.

Copy 1:
Lazy to text? Send voice messages in just 1 click.
Download vokra now!

Copy 2:
Turn your phone into a walkie talkie. vokra!
Download the free app today!

Reason: Extending timeline so that I can provide designers with more time to think this through.

Hi All,
I have just extended the deadline to this brief and has up my contest prize amount.
I have also uploaded a mock up of what the app website will look like.

Any further questions, please feel free to give me a shout.

Thanks for your interest.

Hi,
I am working on a launch of a new app with its core feature - voice messaging.
I need banner ads for both mobile and online, details are within the brief.

I need a very strong designer to help me out here with the banner design to "vamp" up my product.

Any questions, please feel free to give me a shout.

Thanks all for your interest.

Reason: Extended the timeline as I couldn't get the design that I wanted

Target Market(s)

Anyone who has a Cirravine account can use this app to communicate to their friends. It works like a walkie talkie.

Requirements
Must have
• 1) vokra logo

```html
<!DOCTYPE html>
<html lang="en">
<head>
<meta charset="utf-8">
<title>vokra banner set – copy 2</title>
<link rel="stylesheet" href="https://fonts.googleapis.com/css2?family=Source+Sans+3:wght@300;400;600;700&display=swap">
<style>
  :root {
    --page: #ffffff;
    --ink: #1d1d1d;
    --sky-light: #4fb0dc;
    --sky-mid: #2a8cc2;
    --sky-deep: #0f5d90;
    --brand-red: #d5262b;
    --white: #ffffff;
    --wordmark: #eef4f8;
    --button-top: #ffffff;
    --button-bottom: #d9dde0;
    --button-text: #1f1f1f;
    --button-green: #3f9b2f;
    --phone-dark: #2a2e33;
    --phone-screen: #dfe7f0;
  }
  * { box-sizing: border-box; margin: 0; padding: 0; }
  html, body { width: 1200px; height: 833px; overflow: hidden; background: var(--page); }
  body { position: relative; font-family: "Source Sans 3", "Helvetica Neue", Arial, sans-serif; color: var(--ink); }

  .set-label {
    position: absolute; left: 643px; top: 92px;
    font-size: 27px; font-weight: 300; letter-spacing: 0.02em; color: var(--ink);
  }

  .banner {
    --u: 1px;
    position: absolute; overflow: hidden;
    background:
      radial-gradient(ellipse 60% 70% at 45% 35%, rgba(120, 200, 240, 0.55), transparent 70%),
      linear-gradient(180deg, var(--sky-light) 0%, var(--sky-mid) 45%, var(--sky-deep) 100%);
    color: var(--white);
  }
  .banner > * { position: absolute; z-index: 2; }
  .banner > .device { z-index: 1; }

  .brand { display: flex; align-items: center; }
  .brand-dot { display: block; border-radius: 50%; background: var(--brand-red); flex: none; }
  .brand-name { font-weight: 700; color: var(--white); line-height: 1; }

  .wordmark { font-weight: 300; color: var(--wordmark); line-height: 1; white-space: nowrap; text-shadow: 0 1px 3px rgba(0, 40, 80, 0.35); }
  .tagline { font-weight: 700; line-height: 1.15; white-space: nowrap; text-shadow: 0 1px 2px rgba(0, 40, 80, 0.35); }

  .cta {
    display: flex; align-items: center;
    background: linear-gradient(180deg, var(--button-top) 0%, var(--button-top) 45%, var(--button-bottom) 100%);
    color: var(--button-text);
    white-space: nowrap;
    box-shadow: 0 1px 3px rgba(0, 30, 60, 0.35);
  }
  .cta-icon { flex: none; }
  .cta-accent { color: var(--button-green); }
  .cta-copy { display: flex; flex-direction: column; align-items: center; line-height: 1; }
  .pointer { display: block; }

  .device {
    background: linear-gradient(165deg, var(--phone-dark) 0%, #4a5158 24%, var(--phone-screen) 25%, #c9d6e4 100%);
    box-shadow: 0 0 0 calc(var(--u) * 4) #1c1f23;
  }

  /* ---------- 300 x 250 ---------- */
  .banner-medium { --u: 1.45px; left: 51px; top: 91px; width: calc(var(--u) * 300); height: calc(var(--u) * 250); }
  .banner-medium .brand { left: calc(var(--u) * 10); top: calc(var(--u) * 12); gap: calc(var(--u) * 6); }
  .banner-medium .brand-dot { width: calc(var(--u) * 26); height: calc(var(--u) * 26); }
  .banner-medium .brand-name { font-size: calc(var(--u) * 30); }
  .banner-medium .device { left: calc(var(--u) * 214); top: calc(var(--u) * 4); width: calc(var(--u) * 140); height: calc(var(--u) * 280); border-radius: calc(var(--u) * 20) 0 0 0; transform: rotate(-10deg); transform-origin: top left; }
  .banner-medium .wordmark { left: calc(var(--u) * 12); top: calc(var(--u) * 78); font-size: calc(var(--u) * 64); }
  .banner-medium .tagline { left: calc(var(--u) * 17); top: calc(var(--u) * 140); font-size: calc(var(--u) * 16); }
  .banner-medium .cta { left: calc(var(--u) * 16); top: calc(var(--u) * 189); width: calc(var(--u) * 170); height: calc(var(--u) * 46); border-radius: calc(var(--u) * 7); padding-left: calc(var(--u) * 8); gap: calc(var(--u) * 8); }
  .banner-medium .cta-icon { width: calc(var(--u) * 22); height: calc(var(--u) * 24); }
  .banner-medium .cta-small { font-size: calc(var(--u) * 9.5); font-weight: 600; }
  .banner-medium .cta-large { font-size: calc(var(--u) * 20); font-weight: 600; margin-top: calc(var(--u) * 2); }
  .banner-medium .pointer { left: calc(var(--u) * 170); top: calc(var(--u) * 214); width: calc(var(--u) * 24); height: calc(var(--u) * 28); }

  /* ---------- strip banners (units of a 50-high frame) ---------- */
  .banner-strip { height: calc(var(--u) * 50); }
  .banner-strip .brand { left: calc(var(--u) * 5); top: calc(var(--u) * 18); gap: calc(var(--u) * 3); }
  .banner-strip .brand-dot { width: calc(var(--u) * 11); height: calc(var(--u) * 11); }
  .banner-strip .brand-name { font-size: calc(var(--u) * 13); }
  .banner-strip .tagline { left: calc(var(--u) * 57); top: calc(var(--u) * 3); font-size: calc(var(--u) * 11.5); font-weight: 600; text-transform: uppercase; }
  .banner-strip .wordmark { left: calc(var(--u) * 57); top: calc(var(--u) * 19); font-size: calc(var(--u) * 26); font-weight: 400; }
  .banner-strip .cta { left: calc(var(--u) * 136); right: calc(var(--u) * 5); top: calc(var(--u) * 21); height: calc(var(--u) * 26); border-radius: calc(var(--u) * 4); padding-left: calc(var(--u) * 6); gap: calc(var(--u) * 5); }
  .banner-strip .cta-icon { width: calc(var(--u) * 13); height: calc(var(--u) * 14); }
  .banner-strip .cta-text { font-size: calc(var(--u) * 8.6); font-weight: 600; }

  .strip-wide { width: calc(var(--u) * 320); }
  .strip-narrow { width: calc(var(--u) * 300); }
  .strip-narrow .tagline { font-size: calc(var(--u) * 10.6); }
  .strip-narrow .cta { left: calc(var(--u) * 130); }

  .strip-120 { --u: 0.58px; left: 643px; top: 274px; }
  .strip-168 { --u: 0.82px; left: 643px; top: 332px; }
  .strip-216 { --u: 1.04px; left: 643px; top: 401px; }
  .strip-320 { --u: 1.45px; left: 643px; top: 489px; }
  .strip-300 { --u: 1.45px; left: 51px; top: 489px; }

  /* ---------- 728 x 90 ---------- */
  .banner-leader { --u: 1.45px; left: 51px; top: 604px; width: calc(var(--u) * 728); height: calc(var(--u) * 90); }
  .banner-leader .brand { left: calc(var(--u) * 14); top: calc(var(--u) * 30); gap: calc(var(--u) * 6); }
  .banner-leader .brand-dot { width: calc(var(--u) * 24); height: calc(var(--u) * 24); }
  .banner-leader .brand-name { font-size: calc(var(--u) * 28); }
  .banner-leader .wordmark { left: calc(var(--u) * 180); top: calc(var(--u) * 6); font-size: calc(var(--u) * 58); }
  .banner-leader .tagline { left: calc(var(--u) * 115); top: calc(var(--u) * 61); font-size: calc(var(--u) * 17); }
  .banner-leader .device { left: calc(var(--u) * 410); top: calc(var(--u) * 2); width: calc(var(--u) * 138); height: calc(var(--u) * 110); border-radius: calc(var(--u) * 18) calc(var(--u) * 18) 0 0; transform: rotate(-6deg); transform-origin: top left; }
  .banner-leader .cta { left: calc(var(--u) * 545); top: calc(var(--u) * 21); width: calc(var(--u) * 172); height: calc(var(--u) * 52); border-radius: calc(var(--u) * 7); padding-left: calc(var(--u) * 10); gap: calc(var(--u) * 8); }
  .banner-leader .cta-icon { width: calc(var(--u) * 22); height: calc(var(--u) * 24); }
  .banner-leader .cta-small { font-size: calc(var(--u) * 10); font-weight: 600; }
  .banner-leader .cta-large { font-size: calc(var(--u) * 19); font-weight: 600; margin-top: calc(var(--u) * 1); }
  .banner-leader .pointer { left: calc(var(--u) * 700); top: calc(var(--u) * 50); width: calc(var(--u) * 24); height: calc(var(--u) * 28); }
</style>
</head>
<body>

<svg width="0" height="0" style="position:absolute">
  <defs>
    <symbol id="icon-chevrons" viewBox="0 0 22 24">
      <path d="M2 2 L11 10 L20 2 L20 8 L11 16 L2 8 Z" fill="#5fb83e"/>
      <path d="M2 10 L11 18 L20 10 L20 16 L11 24 L2 16 Z" fill="#3f9b2f"/>
    </symbol>
    <symbol id="icon-pointer" viewBox="0 0 24 28">
      <path d="M2 2 L2 22 L7 17 L11 26 L15 24 L11 16 L18 16 Z" fill="#ffffff" stroke="#333" stroke-width="1.6" stroke-linejoin="round"/>
    </symbol>
  </defs>
</svg>

<p class="set-label">TEXT COPY 2</p>

<!-- 300 x 250 -->
<section class="banner banner-medium">
  <div class="brand"><span class="brand-dot"></span><span class="brand-name">vokra</span></div>
  <div class="device" role="img" aria-label="Smartphone showing the vokra app message screen"></div>
  <h2 class="wordmark">vokra!</h2>
  <p class="tagline">Turn your phone into<br>a walkie talkie.</p>
  <div class="cta">
    <svg class="cta-icon"><use href="#icon-chevrons"/></svg>
    <span class="cta-copy"><span class="cta-small">DOWNLOAD THE FREE APP</span><span class="cta-large">TODAY!</span></span>
  </div>
  <svg class="pointer"><use href="#icon-pointer"/></svg>
</section>

<!-- mobile strips -->
<section class="banner banner-strip strip-wide strip-120">
  <div class="brand"><span class="brand-dot"></span><span class="brand-name">vokra</span></div>
  <p class="tagline">Turn your phone into a walkie talkie.</p>
  <h2 class="wordmark">vokra!</h2>
  <div class="cta"><svg class="cta-icon"><use href="#icon-chevrons"/></svg><span class="cta-text"><span class="cta-accent">DOWNLOAD THE</span> FREE APP TODAY!</span></div>
</section>

<section class="banner banner-strip strip-wide strip-168">
  <div class="brand"><span class="brand-dot"></span><span class="brand-name">vokra</span></div>
  <p class="tagline">Turn your phone into a walkie talkie.</p>
  <h2 class="wordmark">vokra!</h2>
  <div class="cta"><svg class="cta-icon"><use href="#icon-chevrons"/></svg><span class="cta-text"><span class="cta-accent">DOWNLOAD THE</span> FREE APP TODAY!</span></div>
</section>

<section class="banner banner-strip strip-wide strip-216">
  <div class="brand"><span class="brand-dot"></span><span class="brand-name">vokra</span></div>
  <p class="tagline">Turn your phone into a walkie talkie.</p>
  <h2 class="wordmark">vokra!</h2>
  <div class="cta"><svg class="cta-icon"><use href="#icon-chevrons"/></svg><span class="cta-text"><span class="cta-accent">DOWNLOAD THE</span> FREE APP TODAY!</span></div>
</section>

<section class="banner banner-strip strip-wide strip-320">
  <div class="brand"><span class="brand-dot"></span><span class="brand-name">vokra</span></div>
  <p class="tagline">Turn your phone into a walkie talkie.</p>
  <h2 class="wordmark">vokra!</h2>
  <div class="cta"><svg class="cta-icon"><use href="#icon-chevrons"/></svg><span class="cta-text"><span class="cta-accent">DOWNLOAD THE</span> FREE APP TODAY!</span></div>
</section>

<section class="banner banner-strip strip-narrow strip-300">
  <div class="brand"><span class="brand-dot"></span><span class="brand-name">vokra</span></div>
  <p class="tagline">Turn your phone into a walkie talkie.</p>
  <h2 class="wordmark">vokra!</h2>
  <div class="cta"><svg class="cta-icon"><use href="#icon-chevrons"/></svg><span class="cta-text"><span class="cta-accent">DOWNLOAD THE</span> FREE APP TODAY!</span></div>
</section>

<!-- 728 x 90 -->
<section class="banner banner-leader">
  <div class="brand"><span class="brand-dot"></span><span class="brand-name">vokra</span></div>
  <div class="device" role="img" aria-label="Smartphone showing the vokra app message screen"></div>
  <h2 class="wordmark">vokra!</h2>
  <p class="tagline">Turn your phone into a walkie talkie.</p>
  <div class="cta">
    <svg class="cta-icon"><use href="#icon-chevrons"/></svg>
    <span class="cta-copy"><span class="cta-small">DOWNLOAD THE FREE APP</span><span class="cta-large">TODAY!</span></span>
  </div>
  <svg class="pointer"><use href="#icon-pointer"/></svg>
</section>

</body>
</html>
```